Clinician manual

I need an expert eye to improve the look and flow of a manual. No content changes on look and feel. We want a sharp professional look. End product will be 8.5x 11 and downloadable from our website. Specifically we need you to..

1- Go through the current clinician manual and organize the information in a way that flows well, and will be easy for the clinician to read and navigate through.
2- After this is done, create your table of contents chronologically to match the flow of the information you’ve laid out for them. (I would highly recommend getting rid of the chapter numbers such as 7, 7.1, 7,2, these can be a bit overwhelming to readers and confusing at first glance.) Then just indicate the page where each topic can be found. Bullet points can be used to indicate additional subjects under a topic (page) heading.
3- Take out the notes that are along the side of the pages that indicate where images, etc. should go, and leave blank spaces within the document.

Target Market(s)

The end user are speech language pathologists in specialized clinical settings. We want it to be a functional, functional, functional product. We also want it to look pretty. It's not a ton we need done we are just swamped and are on a deadline. No content changes needed just design.

Industry/Entity Type

Product

Requirements
Must have
• Did I mention functional? Easy of use is a big goal. Sharp eyes needed.
Nice to have
• End product should be standard paper size (8.5x11) so people can download and print easily.
Should not have
• Overly complicated. We want to be able to edit this ourselves later down the line.

```html
<!DOCTYPE html>
<html lang="en">
<head>
<meta charset="utf-8">
<title>VoxRenew Clinician Manual</title>
<link rel="stylesheet" href="https://fonts.googleapis.com/css2?family=Tinos:ital,wght@0,400;0,700;1,400;1,700&display=swap">
<style>
  :root {
    --paper: #ffffff;
    --ink: #1b1b1b;
    --ink-soft: #111111;
    --accent-gold: #b58d4f;
    --rule-blue: #5b8fd0;
    --photo-light: #eef1ef;
    --photo-mid: #c9cfcc;
    --photo-warm: #d9c4a2;
    --photo-blue: #6b86b8;
  }
  html, body {
    margin: 0;
    padding: 0;
    overflow: hidden;
    background: var(--paper);
  }
  .cover {
    position: relative;
    width: 849px;
    height: 1200px;
    background: var(--paper);
    font-family: "Tinos", "Times New Roman", serif;
    color: var(--ink);
    overflow: hidden;
  }
  .brand {
    position: absolute;
    top: 236px;
    left: 0;
    width: 849px;
    display: flex;
    justify-content: center;
    align-items: center;
    gap: 18px;
  }
  .brand-mark {
    width: 46px;
    height: 46px;
    border-radius: 50%;
    background: var(--accent-gold);
  }
  .brand-name {
    font-weight: 700;
    font-size: 64px;
    letter-spacing: 2px;
    color: var(--ink);
    line-height: 1;
  }
  .tagline {
    position: absolute;
    top: 330px;
    left: 0;
    width: 849px;
    margin: 0;
    text-align: center;
    font-size: 24px;
    font-weight: 700;
    font-style: italic;
    color: var(--ink-soft);
  }
  .hero-photo {
    position: absolute;
    top: 408px;
    left: 102px;
    width: 647px;
    height: 432px;
    background:
      linear-gradient(180deg, var(--photo-light) 0%, var(--photo-light) 35%, var(--photo-warm) 62%, var(--photo-mid) 100%),
      var(--photo-mid);
  }
  .hero-photo::after {
    content: "";
    position: absolute;
    inset: 0;
    background: linear-gradient(90deg, rgba(107,134,184,0.35) 0%, rgba(255,255,255,0) 40%, rgba(255,255,255,0) 70%, rgba(107,134,184,0.45) 100%);
  }
  .title {
    position: absolute;
    top: 896px;
    left: 0;
    width: 849px;
    margin: 0;
    text-align: center;
    font-size: 40px;
    font-weight: 400;
    font-style: italic;
    color: var(--ink-soft);
  }
  .title-rule {
    position: absolute;
    top: 945px;
    left: 97px;
    width: 652px;
    height: 2px;
    background: var(--rule-blue);
  }
</style>
</head>
<body>
  <main class="cover">
    <div class="brand">
      <span class="brand-mark"></span>
      <span class="brand-name">VoxRenew</span>
    </div>
    <p class="tagline">Reviving Speech and Improving Lives</p>
    <div class="hero-photo" role="img" aria-label="Photograph of four colleagues smiling around a light wood conference table in a bright office"></div>
    <h1 class="title">Clinician Manual</h1>
    <div class="title-rule"></div>
  </main>
</body>
</html>
```